KelvrasMassage website required

We need a website for a mobile sports massage therapist in the United Kingdom. Specialising in pregnancy and postnatal massage, sports and remedial, deep tissue massage & Corprate Massage. Attached are some logos that we already have in various colours. The file named logo_white_background is what we normally use. Feel free to use the others at your discretion.

Requirements
Must have
• Service areas, Booking system.

```html
<!DOCTYPE html>
<html lang="en">
<head>
<meta charset="utf-8">
<title>Kelvras Massage</title>
<link href="https://fonts.googleapis.com/css2?family=Open+Sans:wght@400;600;700&family=Oswald:wght@600;700&family=Roboto:wght@400;500;700;900&display=swap" rel="stylesheet">
<style>
:root{
  --green:#95c821;
  --green-dark:#7fae14;
  --navy:#0d4766;
  --ink:#2a2a2a;
  --muted:#6f6f6f;
  --dark:#343434;
  --panel:#e8e8e8;
  --form-border:#183a1c;
  --input-border:#4b7f86;
}
*{margin:0;padding:0;box-sizing:border-box}
html,body{width:1200px;height:2469px;overflow:hidden}
body{position:relative;background:#fff;font-family:"Open Sans",Arial,sans-serif;color:var(--ink)}
.abs{position:absolute}

/* header */
.topbar{left:0;top:0;width:1200px;height:85px;background:var(--green)}
.brand{left:173px;top:0;width:123px;height:110px;background:#fff;display:flex;flex-direction:column;align-items:center;justify-content:center;gap:6px;box-shadow:0 2px 6px rgba(0,0,0,.15)}
.brand-name{font-family:"Roboto",sans-serif;font-weight:700;font-size:17px;color:#3d8fb8;line-height:1.1;text-align:center}
.brand-dot{width:12px;height:12px;border-radius:50%;background:#3d8fb8}
.mainnav{left:459px;top:23px;width:423px;height:40px;background:var(--navy);display:flex;align-items:center;justify-content:space-around;padding:0 10px}
.mainnav a{color:#fff;text-decoration:none;font-family:"Roboto",sans-serif;font-size:12.5px;font-weight:500}
.phone{left:905px;top:30px;display:flex;align-items:center;gap:12px;color:#fff;font-family:"Roboto",sans-serif;font-size:13px}

/* hero */
.hero{left:0;top:85px;width:1200px;height:417px;background:linear-gradient(180deg,#3a3836 0%,#2c2a28 45%,#47423d 100%)}
.hero-title{left:176px;top:196px;font-family:"Oswald",sans-serif;font-weight:700;font-size:44px;line-height:56px;color:#fff;letter-spacing:.5px}
.hero-title em{font-style:normal;color:var(--green)}
.hero-text{left:178px;top:323px;width:440px;font-size:12.6px;line-height:24px;color:#eee}
.video{left:625px;top:163px;width:402px;height:260px;border-radius:6px;background:linear-gradient(135deg,#a9c4d6 0%,#e7eef2 50%,#c6d3db 100%)}
.play{left:800px;top:276px;width:52px;height:36px;border-radius:9px;background:#e62117}

/* steps */
.steps-line{left:199px;top:583px;width:1px;height:238px;background:#cfcfcf}
.step{left:174px;width:430px;height:60px}
.step-icon{position:absolute;left:0;top:0;width:50px;height:50px;border-radius:50%;display:flex;align-items:center;justify-content:center;box-shadow:0 0 0 4px #fff,0 0 0 5px #bbb}
.step-icon.is-active{background:var(--green);box-shadow:0 0 0 4px #fff,0 0 0 5px var(--green)}
.step-icon.is-dark{background:#2e2e2e}
.step-bracket{position:absolute;left:72px;top:6px;width:8px;height:38px;border-left:1px solid #bbb}
.step-bracket::before{content:"";position:absolute;left:-22px;top:18px;width:22px;height:1px;background:#bbb}
.step h4{position:absolute;left:94px;top:-8px;font-family:"Roboto",sans-serif;font-size:13px;font-weight:700;color:#222}
.step p{position:absolute;left:94px;top:12px;width:330px;font-size:11px;line-height:17px;color:var(--muted)}

/* appointment */
.appt-title{left:673px;top:532px;font-family:"Roboto",sans-serif;font-size:24px;font-weight:700;color:#222}
.appt-rule{left:673px;top:576px;width:90px;height:1px;background:#bbb}
.appt-form{left:675px;top:616px;width:352px;height:302px;border:4px solid var(--form-border);background:#fff}
.field{position:absolute;height:33px;border:1.5px solid var(--input-border);font-size:10px;color:#777;padding:0 12px;display:flex;align-items:center;justify-content:space-between}
.field.area{align-items:flex-start;padding-top:10px}
.send{position:absolute;left:14px;top:236px;width:81px;height:30px;background:#1e2a36;color:#fff;font-size:9px;font-weight:700;display:flex;align-items:center;justify-content:center}

/* section headings */
.sec-title{left:0;width:1200px;text-align:center;font-family:"Roboto",sans-serif;font-weight:900;font-size:28px;color:#2a2a2a;letter-spacing:.5px}
.sec-rule{left:585px;width:30px;height:3px;background:#2a2a2a}
.sec-desc{left:400px;width:400px;text-align:center;font-size:11.5px;line-height:18px;color:#444}

/* services */
.svc{top:1123px;width:270px;height:362px;border:1.5px solid var(--green)}
.svc.is-featured{background:var(--green)}
.svc-card{position:absolute;left:15px;top:15px;width:237px;height:330px;background:#fff;box-shadow:0 3px 10px rgba(0,0,0,.22);text-align:center}
.svc-photo{position:absolute;left:26px;top:22px;width:185px;height:122px;box-shadow:4px 6px 10px rgba(0,0,0,.25)}
.svc-card h3{position:absolute;left:0;top:172px;width:100%;font-size:12px;font-weight:600;color:#222}
.svc-card .rule{position:absolute;left:108px;top:198px;width:22px;height:1px;background:#333}
.svc-card p{position:absolute;left:18px;top:212px;width:201px;font-size:12px;line-height:20px;color:#444}
.svc-btn{position:absolute;left:74px;top:287px;width:90px;height:28px;border:1px solid var(--green);border-radius:14px;font-size:9px;color:var(--green);display:flex;align-items:center;justify-content:center}
.svc.is-featured .svc-btn{background:var(--green);color:#fff}

/* team */
.member{top:1671px;width:197px;height:260px;text-align:center}
.member-photo{position:absolute;left:0;top:0;width:197px;height:194px}
.member-social{position:absolute;left:0;top:171px;width:197px;height:23px;background:var(--green);display:flex;justify-content:center;align-items:center;gap:14px}
.member-social span{width:7px;height:7px;border-radius:50%;background:#fff}
.member-info{position:absolute;left:0;top:194px;width:197px;height:66px;padding-top:16px;border-bottom:1px solid #e2e2e2}
.member.is-active .member-info{background:#2f3540;border:none}
.member-info h5{font-size:13px;font-weight:400;color:#333}
.member-info small{display:block;font-size:9px;color:#777;margin-top:2px}
.member.is-active h5,.member.is-active small{color:#fff}

/* commitment & testimonials */
.panel{left:0;top:1985px;width:1200px;height:326px;background:var(--panel)}
.panel-title{font-family:"Roboto",sans-serif;font-weight:900;font-size:19px;color:#222;letter-spacing:.3px}
.panel-title em{font-style:normal;color:var(--green)}
.commit-text{left:155px;top:2072px;width:430px;font-size:12.5px;line-height:21px;color:#222}
.ticks{left:155px;top:2150px;list-style:none}
.ticks li{display:flex;align-items:center;gap:10px;font-size:12.5px;height:31px;color:#222}
.tick{width:14px;height:14px;border-radius:50%;background:var(--green);display:flex;align-items:center;justify-content:center}
.divider{left:594px;top:2058px;width:1px;height:230px;background:#c9c9c9}
.arrow{top:2025px;width:23px;height:23px;border:1px solid #bbb;background:#fff;display:flex;align-items:center;justify-content:center}
.quote{left:625px;top:2077px;width:407px;height:110px;background:#fff;border-radius:8px;padding:14px 18px 0 30px;font-size:11.5px;line-height:19px;font-style:italic;color:#333}
.quote-mark{position:absolute;left:12px;top:4px;font-family:Georgia,serif;font-size:34px;color:#c8c8c8;font-style:normal}
.quote-tail{left:968px;top:2186px}
.avatar{left:645px;top:2225px;width:60px;height:60px;border-radius:50%;background:linear-gradient(160deg,#6d6d6d,#2e2e2e);border:3px solid #fff}
.client{left:724px;top:2247px;font-size:11px;font-weight:700;color:var(--green)}

/* footer */
.foot-nav{left:0;top:2311px;width:1200px;height:61px;background:var(--green)}
.foot-links{left:156px;top:2333px;display:flex;gap:18px;color:#fff;font-family:"Roboto",sans-serif;font-size:14px;font-weight:500}
.follow{left:856px;top:2327px;color:#fff;font-family:"Roboto",sans-serif;font-size:20px;font-weight:500}
.social{top:2328px;width:27px;height:27px;border-radius:50%;background:#fff}
.foot{left:0;top:2372px;width:1200px;height:97px;background:var(--dark)}
.contact{top:2400px;display:flex;align-items:center;gap:12px;color:#fff}
.contact-icon{width:28px;height:28px;border-radius:50%;background:var(--green);display:flex;align-items:center;justify-content:center}
.contact strong{display:block;font-size:14px;font-weight:600}
.contact small{display:block;font-size:9px;color:#ddd}
.legal{left:800px;top:2390px;width:240px;text-align:center;color:#fff}
.legal strong{display:block;font-family:"Roboto",sans-serif;font-weight:900;font-size:21px;letter-spacing:.5px}
.legal small{display:block;font-size:10px;line-height:18px}
</style>
</head>
<body>

<header>
  <div class="abs topbar"></div>
  <div class="abs brand"><span class="brand-dot"></span><span class="brand-name">Kelvra's<br>Massage</span></div>
  <nav class="abs mainnav">
    <a>HOME</a><a>ABOUT US</a><a>SERVICES ▾</a><a>INQUIRY</a><a>CONTACT US</a>
  </nav>
  <div class="abs phone">
    <svg width="20" height="16" viewBox="0 0 20 16"><path d="M2 5c0-3 16-3 16 0v2h-4V5H6v2H2z M4 8h12l2 7H2z" fill="#fff"/></svg>
    <span>024 681 357</span>
  </div>
</header>

<section>
  <div class="abs hero" role="img" aria-label="Photo of a dim conference room with large windows"></div>
  <h1 class="abs hero-title"><em>PREGNANCY</em> AND<br><em>POSTNATAL</em> MASSAGE</h1>
  <p class="abs hero-text">Sed ut perspiciatis unde omnis iste natus error sit voluptatem accusantium doloremque laudantium, totam rem aperiam, eaque ipsa quae ab illo inventore veritatis et quasi veritatis et quasi architecto beatae vitae dicta sunt explicabo. Sed ut perspiciatis unde omnis iste natus error.</p>
  <div class="abs video" role="img" aria-label="Video still of a clinician performing a pregnancy ultrasound"></div>
  <div class="abs play"><svg width="52" height="36"><path d="M21 11l12 7-12 7z" fill="#fff"/></svg></div>
</section>

<section>
  <div class="abs steps-line"></div>
  <div class="abs step" style="top:558px">
    <div class="step-icon is-active"><svg width="22" height="22"><circle cx="11" cy="11" r="9" fill="none" stroke="#fff" stroke-width="2"/><circle cx="11" cy="11" r="4" fill="#fff"/></svg></div>
    <span class="step-bracket"></span>
    <h4>Research</h4>
    <p>Duis autem vel eum iriure dolor in hendrerit in vulputate velit esse molestie consequat vel illum dolore</p>
  </div>
  <div class="abs step" style="top:678px">
    <div class="step-icon is-dark"><svg width="22" height="22"><path d="M4 4l14 14M18 4L4 18" stroke="#fff" stroke-width="2.5"/></svg></div>
    <span class="step-bracket"></span>
    <h4>Make Work</h4>
    <p>Duis autem vel eum iriure dolor in hendrerit in vulputate velit esse molestie consequat vel illum dolore</p>
  </div>
  <div class="abs step" style="top:796px">
    <div class="step-icon is-dark"><svg width="22" height="22"><circle cx="11" cy="11" r="9" fill="none" stroke="#fff" stroke-width="2"/><path d="M6 11l4 4 7-8" fill="none" stroke="#fff" stroke-width="2"/></svg></div>
    <span class="step-bracket"></span>
    <h4>Success</h4>
    <p>Duis autem vel eum iriure dolor in hendrerit in vulputate velit esse molestie consequat vel illum dolore</p>
  </div>

  <h2 class="abs appt-title">Make An Appointment</h2>
  <div class="abs appt-rule"></div>
  <form class="abs appt-form">
    <div class="field" style="left:14px;top:30px;width:151px">Full Name</div>
    <div class="field" style="left:172px;top:30px;width:151px">Email Address</div>
    <div class="field" style="left:14px;top:83px;width:151px">Select Date</div>
    <div class="field" style="left:172px;top:83px;width:151px">Select Category <span>▾</span></div>
    <div class="field area" style="left:14px;top:134px;width:309px;height:82px">message</div>
    <div class="send">SEND</div>
  </form>
</section>

<section>
  <h2 class="abs sec-title" style="top:986px">SERVICES</h2>
  <div class="abs sec-rule" style="top:1031px"></div>
  <p class="abs sec-desc" style="top:1042px">Sed ut perspiciatis unde omnis iste natus error sitvoluptatem accusantium doloremque laudantium.</p>

  <div class="abs svc" style="left:173px">
    <div class="svc-card">
      <div class="svc-photo" style="background:linear-gradient(135deg,#e9e4e6,#d77fb0 60%,#c9c2c4)" role="img" aria-label="Photo of a pregnant woman stretching with a partner"></div>
      <h3>Pregnancy and Postnatal Massage</h3><span class="rule"></span>
      <p>Lorem ipsum dolor sit amet, con-sectetuer adipiscing elit, dolore magna aliquam erat volutpat..</p>
      <div class="svc-btn">View Details</div>
    </div>
  </div>
  <div class="abs svc is-featured" style="left:466px">
    <div class="svc-card">
      <div class="svc-photo" style="background:linear-gradient(180deg,#c9d8e4,#7f8f9c 60%,#6a6660)" role="img" aria-label="Photo of two runners on a seaside promenade"></div>
      <h3>Sports and Remedial</h3><span class="rule"></span>
      <p>Lorem ipsum dolor sit amet, con-sectetuer adipiscing elit, dolore magna aliquam erat volutpat..</p>
      <div class="svc-btn">View Details</div>
    </div>
  </div>
  <div class="abs svc" style="left:757px">
    <div class="svc-card">
      <div class="svc-photo" style="background:linear-gradient(135deg,#f1ece8,#c9937a 55%,#8a5a44)" role="img" aria-label="Photo of hands giving a leg massage"></div>
      <h3>Deep Tissue &amp; Corprate Massage</h3><span class="rule"></span>
      <p>Lorem ipsum dolor sit amet, con-sectetuer adipiscing elit, dolore magna aliquam erat volutpat..</p>
      <div class="svc-btn">View Details</div>
    </div>
  </div>
</section>

<section>
  <h2 class="abs sec-title" style="top:1536px">OUR SPECIALITY</h2>
  <div class="abs sec-rule" style="top:1581px"></div>
  <p class="abs sec-desc" style="top:1592px">Sed ut perspiciatis unde omnis iste natus error sitvoluptatem accusantium doloremque laudantium.</p>

  <div class="abs member" style="left:173px">
    <div class="member-photo" style="background:linear-gradient(180deg,#ececec,#7ea6d3)" role="img" aria-label="Portrait of a smiling therapist in a blue shirt"></div>
    <div class="member-info"><h5>Member Name</h5><small>Pregnancy and Postnatal Massage</small></div>
  </div>
  <div class="abs member is-active" style="left:392px">
    <div class="member-photo" style="background:linear-gradient(180deg,#f2f2f2,#5e6165)" role="img" aria-label="Portrait of a therapist in a grey suit"></div>
    <div class="member-social"><span></span><span></span><span></span><span></span></div>
    <div class="member-info"><h5>Member Name</h5><small>Sports and Remedial</small></div>
  </div>
  <div class="abs member" style="left:611px">
    <div class="member-photo" style="background:linear-gradient(180deg,#f2f2f2,#2f5d9a)" role="img" aria-label="Portrait of a therapist with glasses in a blue shirt"></div>
    <div class="member-info"><h5>Member Name</h5><small>Deep Tissue &amp; Corprate Massage</small></div>
  </div>
  <div class="abs member" style="left:831px">
    <div class="member-photo" style="background:linear-gradient(180deg,#dfe6ea,#8fb0d8)" role="img" aria-label="Portrait of a thoughtful therapist in a checked shirt"></div>
    <div class="member-info"><h5>Member Name</h5><small>Sports and Remedial</small></div>
  </div>
</section>

<section>
  <div class="abs panel"></div>
  <h3 class="abs panel-title" style="left:153px;top:2024px">OUR <em>COMMITMENT TO CUSTOMERS</em></h3>
  <p class="abs commit-text">Loren autem vel eum iriure hendrerit in vulputate velit esse molestie. onsectetuer adipiscing elit, sed diam nonummy nibh euismod tincidunt u eu feugiat nulla facilisis.</p>
  <ul class="abs ticks">
    <li><span class="tick"><svg width="8" height="8"><path d="M1 4l2 2 4-5" fill="none" stroke="#fff" stroke-width="1.6"/></svg></span>Autem vel eum iriure hendrerit in</li>
    <li><span class="tick"><svg width="8" height="8"><path d="M1 4l2 2 4-5" fill="none" stroke="#fff" stroke-width="1.6"/></svg></span>Gendrerit in vulputate velit</li>
    <li><span class="tick"><svg width="8" height="8"><path d="M1 4l2 2 4-5" fill="none" stroke="#fff" stroke-width="1.6"/></svg></span>Autem vel eum adipiscing elit, sed diam</li>
    <li><span class="tick"><svg width="8" height="8"><path d="M1 4l2 2 4-5" fill="none" stroke="#fff" stroke-width="1.6"/></svg></span>Eeum iriure hendrerit in vulputate velit</li>
  </ul>
  <div class="abs divider"></div>

  <h3 class="abs panel-title" style="left:625px;top:2024px">CLIENT <em>TESTIMONIALS</em></h3>
  <div class="abs arrow" style="left:979px"><svg width="8" height="10"><path d="M6 1L2 5l4 4" fill="none" stroke="#555" stroke-width="1.5"/></svg></div>
  <div class="abs arrow" style="left:1007px"><svg width="8" height="10"><path d="M2 1l4 4-4 4" fill="none" stroke="#555" stroke-width="1.5"/></svg></div>
  <div class="abs quote"><span class="quote-mark">“</span>Lorem ipsum dolor sit amet consetug e sed diay nibh euismodl tincidunt ut laoreet dolore magam er vol wisi enim ad minim veniam quis nostrud exerci tationorem ipsum dolor sit ametee sed diammmy nibh euismd tincidunt ut laoreet dolore magna aliqur volpatl tiidunt ut laoreet dolore magna aliqur volpatl r sit ametee.</div>
  <svg class="abs quote-tail" width="30" height="22"><path d="M0 0h30L24 20z" fill="#fff"/></svg>
  <div class="abs avatar" role="img" aria-label="Client portrait"></div>
  <div class="abs client">Mr. Dorin Hale</div>
</section>

<footer>
  <div class="abs foot-nav"></div>
  <nav class="abs foot-links"><span>HOME</span><span>|</span><span>ABOUT US</span><span>|</span><span>SERVICES</span><span>|</span><span>INQUIRY</span><span>|</span><span>CONTACT US</span></nav>
  <div class="abs follow">Follow Us:</div>
  <span class="abs social" style="left:966px"></span>
  <span class="abs social" style="left:1004px"></span>

  <div class="abs foot"></div>
  <div class="abs contact" style="left:156px">
    <span class="contact-icon"><svg width="12" height="14"><path d="M6 0a5 5 0 015 5c0 4-5 9-5 9S1 9 1 5a5 5 0 015-5z" fill="#fff"/><circle cx="6" cy="5" r="2" fill="#95c821"/></svg></span>
    <div><strong>Kelvras Massage</strong><small>Your Company Address</small></div>
  </div>
  <div class="abs contact" style="left:404px">
    <span class="contact-icon"><svg width="14" height="14"><path d="M3 1l3 3-2 2c1 2 2 3 4 4l2-2 3 3-2 2C6 13 1 8 1 3z" fill="#fff"/></svg></span>
    <div><strong>Call Us :</strong><small>024.681.357</small></div>
  </div>
  <div class="abs contact" style="left:585px">
    <span class="contact-icon"><svg width="14" height="10"><rect x="0.5" y="0.5" width="13" height="9" fill="none" stroke="#fff"/><path d="M1 1l6 5 6-5" fill="none" stroke="#fff"/></svg></span>
    <div><strong>Email Us :</strong><small>info@kelvrasmail.com</small></div>
  </div>
  <div class="abs legal">
    <strong>KELVRAS MASSAGE</strong>
    <small>© 2018 Kelvras Massage.</small>
    <small>All Rights Reserved.</small>
  </div>
</footer>

</body>
</html>
```